Education portal needs a new Email Creative Design

We could not decide on the creative earlier as we were unable to picture how will it look. Hence, we have added content so that we can choose the best design of all. Below is the content to be used for the email creative:
____________________________________
Did you know that 25% of all Americans have experienced at least one divorce?*
41% of first marriages end in divorce!!*

Over 1 million children are affected by divorce each year*

Become a Marriage and Family therapist - Achieve inner-happiness by helping individuals, families and couples resolve their struggles and enhance their lives.
Family Therapists are trained in various modes of therapy in order to prepare them for work with individuals, families, couples, and groups.

With proper training, you will be able to treat:
• Depression and other Affective Disorders
• Childhood Behavioral and Emotional Disorders
• Marital and Relationship Problems
• Conduct Disorder and Delinquency
• Substance Abuse
• Alcoholism
• Domestic Violence
• Severe Mental Illness
• Physical Illness

You could also qualify for financial aid* from the government to pursue this career..

Secure your life by earning upto $78,580* and attain peace of mind while helping others..

__________________________

These are the links to images we liked, but if you have something better, we would love to see them:
http://www.pictovale.example/photo/seperated-50317294?st=7kq2m81
http://www.pictovale.example/photo/domestic-violence-68204937?st=b4n9x52

We are an education portal offering options of schools, colleges, universities and courses to students and working professionals.

We are looking for an email creative which has great call-to-action; be creative and research more if you wish.
Incorporate call-to-action tabs, make it colorful, include pictures and content.
Also attached are industry standard creatives for your reference, let me know if you have any questions.
Updates

Please see new files uploaded

I have uploaded a new creative made by our design team. Follow similar guidelines

For those who have not submitted their designs, please send us soon. Thanks

We thought a content brief will do more justice to this design contest hence we have updated our brief with new content to create a newer design Please submit your designs soon. Thanks

Target Market(s)

25 to 50 years working professionals

Industry/Entity Type

Government

Font styles to use
Serif
Sans Serif
Decorative
Script

Requirements
Must have
• Call-to-action

```html
<!DOCTYPE html>
<html lang="en">
<head>
<meta charset="utf-8">
<title>Marriage and Family Therapist Career Email</title>
<link rel="stylesheet" href="https://fonts.googleapis.com/css2?family=Mako&family=Arimo:wght@400;700&display=swap">
<style>
  :root {
    --page-bg: #ececec;
    --sheet-bg: #ffffff;
    --sheet-border: #6e1414;
    --tab-top: #2cc6f2;
    --tab-bottom: #0a8fc7;
    --cta-top: #3fd0f7;
    --cta-bottom: #0778b5;
    --cta-edge: #0a6da3;
    --text-dark: #111111;
    --divider: #f2607a;
    --more-top: #ef6a6a;
    --more-bottom: #c51f24;
    --hero-side: #d3e4f1;
    --hero-mid: #f4c384;
    --thumb-frame: #111111;
    --thumb-fill: #9aa9b8;
  }
  * { box-sizing: border-box; margin: 0; padding: 0; }
  html, body { width: 1000px; height: 1200px; overflow: hidden; }
  body {
    position: relative;
    background: var(--page-bg);
    font-family: "Mako", sans-serif;
    color: var(--text-dark);
  }
  .sheet {
    position: absolute;
    left: 12px; top: 12px;
    width: 976px; height: 1162px;
    background: var(--sheet-bg);
    border: 2px solid var(--sheet-border);
  }
  .nav {
    position: absolute;
    left: 151px; top: 27px;
    display: flex; gap: 3px;
  }
  .nav-tab {
    width: 140px; height: 35px;
    display: flex; align-items: center; justify-content: center;
    background: linear-gradient(var(--tab-top), var(--tab-bottom));
    color: #fff;
    font-size: 21px;
    text-decoration: none;
  }
  .hero {
    position: absolute;
    left: 90px; top: 85px;
    width: 830px; height: 465px;
    background: linear-gradient(90deg, var(--hero-side) 0%, var(--hero-mid) 50%, var(--hero-side) 100%);
  }
  .cta {
    position: absolute;
    left: 298px; top: 550px;
    width: 406px; height: 88px;
    border-radius: 44px;
    background: linear-gradient(var(--cta-top), var(--cta-bottom));
    border: 2px solid var(--cta-edge);
    display: flex; align-items: center; justify-content: center; gap: 20px;
    color: #fff;
    font-size: 42px;
    text-decoration: none;
  }
  .cta svg { width: 58px; height: 46px; }
  .headline {
    position: absolute;
    left: 0; top: 662px; width: 1000px;
    text-align: center;
    font-size: 36px;
    font-weight: 400;
  }
  .quote {
    position: absolute;
    left: 60px; width: 880px;
    font-size: 16.2px;
    line-height: 19.5px;
    text-align: justify;
    text-align-last: center;
  }
  .quote-top { top: 710px; }
  .quote-bottom { top: 1017px; }
  .divider {
    position: absolute;
    left: 45px; width: 908px;
    border-top: 1px dashed var(--divider);
  }
  .divider-top { top: 803px; }
  .divider-bottom { top: 980px; }
  .feature {
    position: absolute;
    top: 843px; width: 420px; height: 112px;
  }
  .feature-left { left: 55px; }
  .feature-right { left: 520px; }
  .feature-photo {
    position: absolute; left: 0; top: 0;
    width: 156px; height: 111px;
    border: 3px solid var(--thumb-frame);
    border-radius: 3px;
    background: var(--thumb-fill);
  }
  .feature-text {
    position: absolute; left: 173px; top: 0;
    width: 242px;
    font-family: "Arimo", Arial, sans-serif;
    font-size: 10.8px;
    line-height: 12.3px;
    text-align: justify;
  }
  .more-btn {
    position: absolute; left: 331px; top: 76px;
    width: 84px; height: 27px;
    border-radius: 6px;
    background: linear-gradient(var(--more-top), var(--more-bottom));
    color: #fff;
    font-family: "Arimo", Arial, sans-serif;
    font-size: 12.5px; font-weight: 700;
    text-decoration: none;
    display: flex; align-items: center;
    padding-left: 17px;
  }
  .more-btn svg {
    position: absolute; right: 3px; top: 2px;
    width: 23px; height: 23px;
  }
  .subhead {
    position: absolute;
    left: 0; top: 1108px; width: 1000px;
    text-align: center;
    font-size: 22px;
    font-weight: 400;
  }
  .footnote {
    position: absolute;
    left: 0; top: 1145px; width: 1000px;
    text-align: center;
    font-size: 16px;
  }
</style>
</head>
<body>
  <main class="sheet"></main>

  <nav class="nav">
    <a class="nav-tab" href="#">Text 01</a>
    <a class="nav-tab" href="#">Text 02</a>
    <a class="nav-tab" href="#">Text 03</a>
    <a class="nav-tab" href="#">Text 04</a>
    <a class="nav-tab" href="#">Text 05</a>
  </nav>

  <div class="hero" role="img" aria-label="Photo of a cheerful student carrying a stack of binders in front of a group of classmates"></div>

  <a class="cta" href="#">
    <svg viewBox="0 0 58 46" aria-hidden="true">
      <polyline points="26,5 8,23 26,41" fill="none" stroke="#fff" stroke-width="8" stroke-linecap="round" stroke-linejoin="round"/>
      <polyline points="50,5 32,23 50,41" fill="none" stroke="#fff" stroke-width="8" stroke-linecap="round" stroke-linejoin="round"/>
    </svg>
    <span>Learn More</span>
    <svg viewBox="0 0 58 46" aria-hidden="true">
      <polyline points="8,5 26,23 8,41" fill="none" stroke="#fff" stroke-width="8" stroke-linecap="round" stroke-linejoin="round"/>
      <polyline points="32,5 50,23 32,41" fill="none" stroke="#fff" stroke-width="8" stroke-linecap="round" stroke-linejoin="round"/>
    </svg>
  </a>

  <h1 class="headline">Become a Marriage and Family Therapist.</h1>

  <p class="quote quote-top">"Did you know that 25% of all Americans have experienced at least one divorce?* 41% of first marriages end in divorce!!* Over 1 million children are affected by divorce each year.* Become a Marriage and Family therapist and achieve inner-happiness by helping individuals, families and couples resolve their struggles and enhance their lives."</p>

  <div class="divider divider-top"></div>

  <section class="feature feature-left">
    <div class="feature-photo" role="img" aria-label="Photo of smiling students holding books"></div>
    <p class="feature-text">Family Therapists are trained in various modes of therapy in order to prepare them for work with individuals, families, couples, and groups. Gain the skills to guide people through their hardest moments .....</p>
    <a class="more-btn" href="#">More
      <svg viewBox="0 0 23 23" aria-hidden="true">
        <circle cx="11.5" cy="11.5" r="10.5" fill="#fff"/>
        <polyline points="9,6 14.5,11.5 9,17" fill="none" stroke="#d0282c" stroke-width="3" stroke-linecap="round" stroke-linejoin="round"/>
      </svg>
    </a>
  </section>

  <section class="feature feature-right">
    <div class="feature-photo" role="img" aria-label="Photo of smiling students holding books"></div>
    <p class="feature-text">With proper training, you will be able to treat depression and other affective disorders, childhood behavioral and emotional disorders, marital and relationship problems, conduct disorder and delinquency ....</p>
    <a class="more-btn" href="#">More
      <svg viewBox="0 0 23 23" aria-hidden="true">
        <circle cx="11.5" cy="11.5" r="10.5" fill="#fff"/>
        <polyline points="9,6 14.5,11.5 9,17" fill="none" stroke="#d0282c" stroke-width="3" stroke-linecap="round" stroke-linejoin="round"/>
      </svg>
    </a>
  </section>

  <div class="divider divider-bottom"></div>

  <p class="quote quote-bottom">"Help people overcome substance abuse, alcoholism, domestic violence, severe mental illness and physical illness. You could also qualify for financial aid* from the government to pursue this career. Choose from schools, colleges, universities and courses built for working professionals and start making a difference in the lives of families today."</p>

  <h2 class="subhead">Secure your life by earning upto $78,580*</h2>

  <p class="footnote">Attain peace of mind while helping others. Find the right therapy program for you today.</p>
</body>
</html>
```